Chiropractic healthcare group business card

We are a Portland Oregon based chiropractic healthcare group. Looking for a new business card design. Something cutting edge, that shows off our new logo and tag line.Use either of the attached logos.Our tag line = "Who would you be without pain?"I'm open to about anything, impress me!!
Target Market(s)
Chiropractic patients - Auto injury, back pain, sports injuries, neck , shoulder, hip, knee, ankle pain.
Industry/Entity Type
Chiropractic
Contact Information for Business Card
Dr. Bram Holtvick, D.C.
Clinic name - Fernway Chiropractic
2 clinics
location #1
20418 NW Marwick Road
Suite B
North Plains, OR 97133
Location #2
13529 SE Calloway Street
Portland OR 97236
Main phone line 971.555.0143
website : www.FernwayClinics.example
Tag line "Who would you be without pain?"
Colors
Designer to choose colors to be used in the design.
Requirements
Must have
- Use the logo colors -- Want the orange color to be a TRUE orange.
- Both clinic address
- phone number
- website
- personal email - b.holtvick@ReliefBeginsHere.example
- tag line - "Who would you be without pain?"

```html
<!DOCTYPE html>
<html lang="en">
<head>
<meta charset="utf-8">
<title>Fernway Chiropractic – Business Card</title>
<link rel="stylesheet" href="https://fonts.googleapis.com/css2?family=Montserrat:wght@600;700&family=Questrial&display=swap">
<style>
  :root {
    --backdrop: #a4a4a4;
    --card: #262626;
    --card-edge: #1b1b1b;
    --orange: #f47320;
    --logo-grey: #5f5f5f;
    --text-light: #d8d8d8;
    --text-muted: #b9b9b9;
    --white: #ffffff;
  }
  * { box-sizing: border-box; margin: 0; padding: 0; }
  html, body {
    width: 1200px;
    height: 1000px;
    overflow: hidden;
    background: var(--backdrop);
  }
  .canvas {
    position: relative;
    width: 1200px;
    height: 1000px;
    display: flex;
    flex-direction: column;
    align-items: center;
    justify-content: center;
    gap: 44px;
  }
  .card {
    position: relative;
    width: 780px;
    height: 446px;
    background: var(--card);
    border-top: 4px solid var(--orange);
    border-left: 4px solid var(--orange);
    overflow: hidden;
    font-family: "Questrial", "Century Gothic", sans-serif;
  }
  .card__band {
    position: absolute;
    left: 0;
    right: 0;
    bottom: 34px;
    height: 30px;
    background: var(--orange);
    color: var(--white);
    display: flex;
    align-items: center;
    justify-content: center;
    font-size: 18px;
    letter-spacing: 1.2px;
  }
  .card__foot {
    position: absolute;
    left: 0;
    right: 0;
    bottom: 0;
    height: 34px;
    background: var(--card-edge);
  }

  /* Front */
  .brand {
    position: absolute;
    left: 0;
    right: 0;
    top: 120px;
    display: flex;
    align-items: center;
    justify-content: center;
    gap: 22px;
  }
  .brand__mark {
    width: 54px;
    height: 54px;
    background: var(--orange);
  }
  .brand__name {
    font-family: "Montserrat", "Century Gothic", sans-serif;
    font-weight: 700;
    color: var(--logo-grey);
    font-size: 40px;
    letter-spacing: 9px;
    line-height: 1.1;
  }

  /* Back */
  .holder {
    position: absolute;
    left: 46px;
    top: 30px;
  }
  .holder__name {
    font-family: "Montserrat", "Century Gothic", sans-serif;
    font-weight: 700;
    color: var(--orange);
    font-size: 25px;
    letter-spacing: 0.6px;
  }
  .holder__clinic {
    margin-top: 6px;
    color: var(--text-muted);
    font-size: 15px;
    font-style: italic;
    letter-spacing: 1px;
  }
  .brand--small {
    top: 196px;
    left: 60px;
    right: auto;
    flex-direction: column;
    align-items: flex-start;
    gap: 14px;
  }
  .brand--small .brand__mark { width: 40px; height: 40px; }
  .brand--small .brand__name { font-size: 22px; letter-spacing: 4px; }

  .contacts {
    position: absolute;
    left: 384px;
    top: 122px;
    list-style: none;
    display: flex;
    flex-direction: column;
    gap: 20px;
  }
  .contacts__item {
    display: flex;
    align-items: flex-start;
    gap: 18px;
    color: var(--text-light);
    font-size: 17px;
    letter-spacing: 1.1px;
    line-height: 1.35;
  }
  .contacts__icon {
    flex: none;
    width: 22px;
    height: 22px;
    fill: var(--orange);
  }
</style>
</head>
<body>
<main class="canvas">

  <section class="card card--front" aria-label="Card front">
    <div class="brand">
      <span class="brand__mark"></span>
      <span class="brand__name">FERNWAY<br>CHIROPRACTIC</span>
    </div>
    <p class="card__band">“Who would you be without pain?”</p>
    <div class="card__foot"></div>
  </section>

  <section class="card card--back" aria-label="Card back">
    <header class="holder">
      <h1 class="holder__name">Dr. Bram Holtvick (D.C)</h1>
      <p class="holder__clinic">Clinic - Fernway Chiropractic</p>
    </header>

    <div class="brand brand--small">
      <span class="brand__mark"></span>
      <span class="brand__name">FERNWAY<br>CHIROPRACTIC</span>
    </div>

    <ul class="contacts">
      <li class="contacts__item">
        <svg class="contacts__icon" viewBox="0 0 24 24" aria-hidden="true"><path d="M6.6 10.8a15.1 15.1 0 0 0 6.6 6.6l2.2-2.2a1 1 0 0 1 1-.25 11.4 11.4 0 0 0 3.6.57 1 1 0 0 1 1 1V20a1 1 0 0 1-1 1A17 17 0 0 1 3 4a1 1 0 0 1 1-1h3.5a1 1 0 0 1 1 1c0 1.25.2 2.45.57 3.6a1 1 0 0 1-.25 1z"/></svg>
        <span>971.555.0143</span>
      </li>
      <li class="contacts__item">
        <svg class="contacts__icon" viewBox="0 0 24 24" aria-hidden="true"><path d="M12 2a7 7 0 0 0-7 7c0 5.2 7 13 7 13s7-7.8 7-13a7 7 0 0 0-7-7zm0 9.5A2.5 2.5 0 1 1 12 6.5a2.5 2.5 0 0 1 0 5z"/></svg>
        <span>13529 SE Calloway Street<br>Portland OR 97236</span>
      </li>
      <li class="contacts__item">
        <svg class="contacts__icon" viewBox="0 0 24 24" aria-hidden="true"><path d="M12 2a7 7 0 0 0-7 7c0 5.2 7 13 7 13s7-7.8 7-13a7 7 0 0 0-7-7zm0 9.5A2.5 2.5 0 1 1 12 6.5a2.5 2.5 0 0 1 0 5z"/></svg>
        <span>20418 NW Marwick Road<br>suite B,North plains,OR 97133</span>
      </li>
      <li class="contacts__item">
        <svg class="contacts__icon" viewBox="0 0 24 24" aria-hidden="true"><path d="M2 6h20v12H2z M2 6l10 7 10-7" /><path d="M2 5h20v2l-10 7L2 7z" fill="var(--card)"/><path d="M2 5h20l-10 7z"/></svg>
        <span>b.holtvick@ReliefBeginsHere.example</span>
      </li>
    </ul>

    <p class="card__band">www.FernwayClinics.example</p>
    <div class="card__foot"></div>
  </section>

</main>
</body>
</html>
```